Kinesiology undergraduate program needs an infographic

We would like an infographic to creatively and succinctly inform students, faculty, staff, and others about our undergraduate values and competencies (perhaps also integrating our mission and vision). We would like to see a design that incorporates the definition of Kinesiology (the study of human movement) and the colors of our Westbrook State University at Larkfield.

```html
<!DOCTYPE html>
<html lang="en">
<head>
<meta charset="utf-8">
<title>Kinesiology Undergraduate Program</title>
<link href="https://fonts.googleapis.com/css2?family=Lato:wght@400;700;900&display=swap" rel="stylesheet">
<style>
:root{
  --red:#d31f3b;
  --red-deep:#a8152b;
  --purple:#8f3a5e;
  --blue:#3f5c98;
  --teal:#3a6887;
  --grey-band:#f1f1f1;
  --icon-grey:#bdb7b7;
  --text:#3c3c3c;
  --white:#ffffff;
  --frame:#d9d9d9;
}
*{margin:0;padding:0;box-sizing:border-box}
html,body{width:1200px;height:847px;overflow:hidden;background:var(--white)}
body{font-family:"Lato",sans-serif;color:var(--text);position:relative}
.poster{position:absolute;left:320px;top:23px;width:571px;height:807px;border:1px solid var(--frame);background:var(--white);overflow:hidden}
.header{position:absolute;left:0;top:0;width:100%;height:171px;
  background:linear-gradient(100deg,var(--red) 0%,var(--red) 30%,#b8294a 55%,var(--purple) 72%,var(--blue) 100%)}
.header::after{content:"";position:absolute;right:0;bottom:0;width:40%;height:60%;
  background:linear-gradient(to top left,rgba(58,104,135,.55),rgba(58,104,135,0) 70%)}
.intro{position:absolute;left:0;top:171px;width:100%;height:244px;background:var(--grey-band)}
.brand{position:absolute;left:38px;top:36px;color:var(--white);font-weight:900;font-size:8.6px;line-height:9.3px;letter-spacing:.6px;text-transform:uppercase}
.brand-dot{position:absolute;left:33px;top:86px;width:15px;height:15px;border-radius:50%;background:var(--white)}
.runners-art{position:absolute;left:160px;top:30px;width:264px;height:240px;border-radius:48% 52% 40% 45%;
  background:radial-gradient(ellipse at 50% 45%,rgba(150,18,28,.85) 0%,rgba(190,40,45,.6) 40%,rgba(210,70,70,.15) 70%,rgba(210,70,70,0) 80%)}
.runners-shadow{position:absolute;left:180px;top:258px;width:230px;height:20px;border-radius:50%;
  background:radial-gradient(ellipse,rgba(0,0,0,.18),rgba(0,0,0,0) 70%)}
.title{position:absolute;left:0;width:592px;text-align:center;color:var(--white)}
.title-main{top:93px;font-weight:900;font-size:38px;letter-spacing:-1.2px;line-height:40px}
.title-sub{top:132px;font-weight:400;font-size:15.5px;letter-spacing:.1px;line-height:18px}
.pillar{position:absolute;width:76px;height:76px;border-radius:50%;background:var(--red);color:var(--white);
  display:flex;flex-direction:column;justify-content:center;align-items:center;text-align:center;font-size:11.5px;line-height:13.5px}
.pillar b{font-weight:900}
.pillar-text{position:absolute;width:160px;text-align:center;font-size:11.5px;line-height:13.8px;color:var(--text)}
.mission{left:70px;top:214px}
.vision{left:260px;top:255px}
.values{left:443px;top:214px}
.mission-text{left:28px;top:298px}
.vision-text{left:218px;top:338px;width:166px}
.values-text{left:396px;top:298px}
.runner-art{position:absolute;left:0;top:455px;width:210px;height:330px;
  background:linear-gradient(160deg,rgba(160,22,32,.9) 0%,rgba(196,62,58,.8) 45%,rgba(220,140,120,.45) 80%,rgba(255,255,255,0) 100%);
  border-radius:40% 30% 30% 20%}
.runner-ground{position:absolute;left:20px;top:770px;width:190px;height:14px;border-radius:50%;
  background:radial-gradient(ellipse,rgba(0,0,0,.15),rgba(0,0,0,0) 70%)}
.competent-ring{position:absolute;left:59px;top:436px;width:152px;height:152px;border-radius:50%;border:1px solid var(--red)}
.competent{position:absolute;left:63px;top:440px;width:144px;height:144px;border-radius:50%;background:rgba(211,31,59,.88)}
.competent-text{position:absolute;left:119px;top:466px;color:var(--white);font-weight:700;font-size:12px;line-height:14.2px}
.competency{position:absolute;left:235px;width:330px}
.competency .icon{position:absolute;left:0;top:0;width:62px;height:62px;border-radius:50%;background:var(--icon-grey)}
.competency .icon svg{width:62px;height:62px}
.competency h2{position:absolute;left:77px;top:0;font-size:12.2px;font-weight:700;color:var(--red);white-space:nowrap;letter-spacing:-.1px}
.competency ul{position:absolute;top:19px;list-style:none;font-size:9.6px;line-height:14.3px}
.competency li{position:relative;padding-left:13px;white-space:nowrap}
.competency li.dot::before{content:"";position:absolute;left:1px;top:5.5px;width:3px;height:3px;border-radius:50%;background:var(--text)}
.col-a{left:78px}
.col-b{left:217px}
.c1{top:454px}.c2{top:536px}.c3{top:620px}.c4{top:704px}
.c1 .icon{top:0}.c1 h2{top:6px}
.c2 h2{top:6px}.c3 h2{top:6px}.c4 h2{top:6px}
</style>
</head>
<body>
<main class="poster">
  <header class="header"></header>
  <section class="intro"></section>

  <div class="runners-shadow"></div>
  <div class="runners-art" role="img" aria-label="Illustration of three anatomical running figures showing muscles in motion"></div>

  <div class="brand">Westbrook<br>State<br>University<br>at<br>Larkfield</div>
  <div class="brand-dot"></div>

  <h1 class="title title-main">KINESIOLOGY</h1>
  <p class="title title-sub">UNDERGRADUATE PROGRAM</p>

  <div class="pillar mission"><span>OUR</span><b>MISSION</b></div>
  <p class="pillar-text mission-text">To empower undergraduate students to pursue excellence through scientific discovery, clinical practice, and health promotion</p>

  <div class="pillar vision"><span>OUR</span><b>VISION</b></div>
  <p class="pillar-text vision-text">WSUL Kinesiology graduates are leaders who excel in careers that enhance the quality of life of individuals and communities</p>

  <div class="pillar values"><span>OUR</span><b>VALUES</b></div>
  <p class="pillar-text values-text">Student Success,<br>Science, and Service</p>

  <div class="runner-ground"></div>
  <div class="runner-art" role="img" aria-label="Illustration of an anatomical running figure showing the muscular system"></div>
  <div class="competent-ring"></div>
  <div class="competent"></div>
  <p class="competent-text">OUR<br>GRADUATES<br>WILL BE<br>COMPETENT<br>IN...</p>

  <section class="competency c1">
    <div class="icon"><svg viewBox="0 0 62 62" fill="none" stroke="#fff" stroke-width="1.4"><path d="M26 48v-8c-5-3-8-8-8-14 0-8 6-14 14-14s13 6 13 13l3 6-3 1v5h-5v7"/><rect x="13" y="20" width="14" height="12"/><path d="M20 20v12M15 23h3M15 26h3M22 23h3M22 26h3"/></svg></div>
    <h2>THE SCIENCE OF KINESIOLOGY</h2>
    <ul class="col-a">
      <li class="dot">Foundational Concepts of Kinesiology</li>
      <li class="dot">Clinical Application</li>
      <li class="dot">Scientific Communication</li>
    </ul>
  </section>

  <section class="competency c2">
    <div class="icon"><svg viewBox="0 0 62 62" fill="none" stroke="#fff" stroke-width="1.4"><path d="M26 48v-8c-5-3-8-8-8-14 0-8 6-14 14-14s13 6 13 13l3 6-3 1v5h-5v7"/><path d="M22 24c0-3 3-5 6-4 1-3 6-3 7 0 3 0 4 3 3 5 1 2-1 4-3 4h-10c-2 0-4-2-3-5z"/><path d="M28 29v14"/></svg></div>
    <h2>THINKING AND REASONING</h2>
    <ul class="col-a">
      <li class="dot">Critical Thinking</li>
      <li class="dot">Quantitative Reasoning</li>
      <li class="dot">Scientific Inquiry</li>
    </ul>
    <ul class="col-b">
      <li class="dot">Concept Integration</li>
    </ul>
  </section>

  <section class="competency c3">
    <div class="icon"><svg viewBox="0 0 62 62" fill="none" stroke="#fff" stroke-width="1.4"><path d="M26 48v-8c-5-3-8-8-8-14 0-8 6-14 14-14s13 6 13 13l3 6-3 1v5h-5v7"/><path d="M30 20l-6 10h12z"/><circle cx="30" cy="20" r="2"/><circle cx="24" cy="30" r="2"/><circle cx="36" cy="30" r="2"/></svg></div>
    <h2>RELATIONSHIPS AND COMMUNICATION</h2>
    <ul class="col-a">
      <li class="dot">Cultural Competence</li>
      <li class="dot">Professionalism</li>
      <li class="dot">Leadership and Teamwork</li>
    </ul>
    <ul class="col-b">
      <li class="dot">Service Orientation</li>
      <li>Citizenship</li>
    </ul>
  </section>

  <section class="competency c4">
    <div class="icon"><svg viewBox="0 0 62 62" fill="none" stroke="#fff" stroke-width="1.4"><path d="M26 48v-8c-5-3-8-8-8-14 0-8 6-14 14-14s13 6 13 13l3 6-3 1v5h-5v7"/><circle cx="29" cy="26" r="4"/><path d="M29 16v20M19 26h32M47 23l4 3-4 3M26 19l3-3 3 3M26 33l3 3 3-3"/></svg></div>
    <h2>INTRAPERSONAL GROWTH</h2>
    <ul class="col-a">
      <li class="dot">Cultural Humility/Sensitivity</li>
      <li class="dot">Integrity</li>
      <li>Self-Directed</li>
    </ul>
    <ul class="col-b">
      <li class="dot">Dependability</li>
      <li class="dot">Mission Oriented</li>
    </ul>
  </section>
</main>
</body>
</html>
```